An animal window cleaning business card

I want a business card design that includes a logo and tells people I am a WINDOW WASHING COMPANY right away.
Were based in Maine, we do window cleaning, pressure washing, and gutter cleaning. We like Pine trees, the Ocean, state of Maine symbols, Lobsters, Moose, Huskies, etc. My business name is "GLEAM HOUR PANES"
The card could also be designed to look like a gift credit card with a 50$ value.

Target Market(s)

my target audience is older folks with disposable money who live on the ocean or have secondary homes for vacation in Maine

Industry/Entity Type

Cleaning Services

Contact Information for Business Card

2.5x3" plastic if possible.

Font styles to use
Sans Serif

Requirements
Must have
• a symbol, or a logo that tells people I am a window washing company Instantly.
The words GLEAM HOUR, my phone number, my name, MY email
Nice to have
• a lobster holding a squeegee, or a stylized cartoonish version of a human huskie holding a squeegee,
Should not have
• a lighthouse
small hard to read text

```html
<!DOCTYPE html>
<html lang="en">
<head>
<meta charset="utf-8">
<title>Gleam Hour Panes – Business Card</title>
<link rel="stylesheet" href="https://fonts.googleapis.com/css2?family=Bebas+Neue&family=Lato:ital,wght@0,400;0,700;1,400&family=Yellowtail&family=Dancing+Script:wght@700&display=swap">
<style>
  :root {
    --backdrop: #4b4b4b;
    --sky-top: #e4f4fd;
    --sky-bottom: #9fd6f5;
    --brand-blue: #1b8fd6;
    --badge-blue: #0b4fae;
    --ink-navy: #123f9a;
    --ink-black: #111111;
    --back-top: #2286ba;
    --back-bottom: #7cc6ec;
    --white: #ffffff;
  }
  * { box-sizing: border-box; margin: 0; padding: 0; }
  html, body { width: 963px; height: 1200px; overflow: hidden; }
  body { background: var(--backdrop); position: relative; }

  .card {
    position: absolute;
    width: 578px;
    height: 330px;
    border-radius: 16px;
    overflow: hidden;
  }

  /* Front */
  .card-front {
    left: 224px; top: 214px;
    background: linear-gradient(160deg, var(--sky-top) 0%, #c8e9fb 55%, var(--sky-bottom) 100%);
  }
  .splash-art {
    position: absolute;
    left: 0; bottom: 0;
    width: 578px; height: 150px;
    background: linear-gradient(20deg, #1f7fd0 0%, #4aa8e6 40%, rgba(160,214,245,0.4) 75%, rgba(228,244,253,0) 100%);
    clip-path: polygon(0 45%, 45% 60%, 75% 28%, 100% 0, 100% 100%, 0 100%);
  }
  .figure-art {
    position: absolute;
    background: linear-gradient(180deg, #1c1c1c 0%, #050505 100%);
    border-radius: 110px 110px 0 0;
  }
  .card-front .figure-art { left: 30px; top: 70px; width: 200px; height: 260px; }

  .front-title {
    position: absolute;
    left: 176px; top: 52px;
    font-family: "Lato", sans-serif;
    font-weight: 700;
    font-size: 33px;
    color: var(--brand-blue);
    line-height: 1;
    white-space: nowrap;
  }
  .value-badge {
    position: absolute;
    left: 386px; top: 94px;
    width: 136px; height: 136px;
  }
  .value-badge span {
    position: absolute; inset: 0;
    display: flex; align-items: center; justify-content: center;
    font-family: "Bebas Neue", sans-serif;
    font-size: 60px;
    color: var(--white);
    padding-top: 4px;
  }
  .owner-name {
    position: absolute;
    right: 44px; top: 226px;
    font-family: "Yellowtail", "Dancing Script", cursive;
    font-size: 38px;
    color: var(--ink-black);
    line-height: 1;
    white-space: nowrap;
  }
  .phone {
    position: absolute;
    right: 44px; top: 270px;
    font-family: "Lato", sans-serif;
    font-weight: 700;
    font-size: 27px;
    line-height: 1.1;
    color: var(--ink-navy);
    letter-spacing: 0.5px;
  }
  .email {
    position: absolute;
    right: 44px; top: 304px;
    font-family: "Lato", sans-serif;
    font-style: italic;
    font-size: 14px;
    color: var(--ink-navy);
  }

  /* Back */
  .card-back {
    left: 221px; top: 627px;
    width: 580px; height: 331px;
    background: linear-gradient(170deg, var(--back-top) 0%, #4aa3d6 50%, var(--back-bottom) 100%);
  }
  .card-back .figure-art { left: 345px; top: 60px; width: 200px; height: 271px; }

  .service-list {
    position: absolute;
    left: 49px; top: 60px;
    list-style: none;
    font-family: "Lato", sans-serif;
    font-size: 13px;
    color: var(--white);
  }
  .service-list li {
    line-height: 21.7px;
    padding-left: 15px;
    position: relative;
  }
  .service-list li::before {
    content: "";
    position: absolute;
    left: 0; top: 8px;
    width: 6px; height: 6px;
    border-radius: 50%;
    background: var(--white);
  }
  .brand-name {
    position: absolute;
    left: 49px; top: 262px;
    font-family: "Lato", sans-serif;
    font-weight: 700;
    font-size: 28px;
    line-height: 1;
    color: var(--ink-black);
    white-space: nowrap;
  }
</style>
</head>
<body>

<section class="card card-front">
  <div class="splash-art" role="img" aria-label="Blue water splash with bubbles"></div>
  <div class="figure-art" role="img" aria-label="Silhouette of a window cleaner raising a squeegee"></div>
  <h1 class="front-title">GLEAM HOUR PANES</h1>
  <div class="value-badge">
    <svg viewBox="0 0 140 140" width="136" height="136" aria-hidden="true">
      <polygon fill="#0b4fae" points="70,0 78,18 92,4 94,24 111,14 107,34 127,30 117,47 137,50 122,63 140,72 122,81 136,94 116,97 126,115 106,111 110,131 92,121 90,140 78,124 70,140 62,124 50,140 48,121 30,131 34,111 14,115 24,97 4,94 18,81 0,72 18,63 3,50 23,47 13,30 33,34 29,14 46,24 48,4 62,18"/>
    </svg>
    <span>50$</span>
  </div>
  <p class="owner-name">Daniel Brooks</p>
  <p class="phone">555-014-2270</p>
  <p class="email">info@gleamhourpanes.com</p>
</section>

<section class="card card-back">
  <div class="figure-art" role="img" aria-label="Silhouette of a window cleaner raising a squeegee"></div>
  <ul class="service-list">
    <li>Window Washing</li>
    <li>Gutter Cleaning</li>
    <li>Leaf Filter Installation</li>
    <li>Pressure Washing</li>
    <li>Roof Cleaning</li>
  </ul>
  <p class="brand-name">GLEAM HOUR PANES</p>
</section>

</body>
</html>
```